Nuvola Serena packaging design

Hi there,
I'm trying to get an outstanding and unique design for my new product.I'm in baby products business.We are launching an organic,100% burp cloth for our online store. The packaging design is very important to our business.We are looking for something simple and unique.Our brand name is Nuvola Serena which means Serene Cloud in Italian. We also have dolphin prints on the burp cloth. Our burp cloth made of organic, hypoallergenic, breathable and ultra soft 100% cotton.Each box has 5 burp cloth. Its made with love and care for delicate and sensitive baby skin.I will attach samples of the burp cloth colors for you to get an idea about the product.

Target Market(s)

baby product

Requirements
Must have
• Our Logo, PLVA image , and made of organic, hypoallergenic, breathable and ultra soft 100% cotton,has 5 burp cloth. Its made with love and care for delicate and sensitive baby skin.I will attach samples of the burp cloth colors for you to get an idea about the product.
Should not have
• We are looking for something different and can Standout , please to don't make design that has the exact idea of the template that I provide.

```html
<!DOCTYPE html>
<html lang="en">
<head>
<meta charset="utf-8">
<title>Nuvola Serena – Muslin Swaddle Blankets Box Front</title>
<link rel="stylesheet" href="https://fonts.googleapis.com/css2?family=Fredoka:wght@600;700&family=Nunito:ital,wght@1,800;1,900&family=Zilla+Slab:wght@500&display=swap">
<style>
  :root {
    --navy: #2a2f7c;
    --navy-deep: #1f2466;
    --kraft: #c8a069;
    --red: #e21d25;
    --white: #ffffff;
    --mint: #a9e2dc;
    --blush: #f4cfc8;
    --page: #ececec;
    --apple: #e52a2f;
  }
  * { margin: 0; padding: 0; box-sizing: border-box; }
  html, body { width: 859px; height: 1200px; overflow: hidden; background: var(--page); }
  .canvas { position: relative; width: 859px; height: 1200px; }
  .box-front {
    position: absolute; left: 44px; top: 260px;
    width: 770px; height: 680px; overflow: hidden;
    background: var(--navy);
    box-shadow: 0 14px 24px rgba(0,0,0,.22);
  }
  .box-front .panel-shapes { position: absolute; inset: 0; }
  .seal {
    position: absolute; left: 32px; top: 38px; width: 132px; height: 132px;
    border-radius: 50%; background: var(--white);
    border: 3px dashed #9aa0b8;
    display: flex; align-items: center; justify-content: center; text-align: center;
    font-family: "Fredoka", sans-serif; font-weight: 700; font-size: 19px;
    line-height: 1.05; color: var(--navy);
  }
  .baby-tag {
    position: absolute; left: 150px; top: 172px;
    font-family: "Fredoka", sans-serif; font-weight: 700; font-size: 22px;
    letter-spacing: 6px; color: var(--red);
  }
  .brand-name {
    position: absolute; left: 38px; top: 198px;
    font-family: "Fredoka", sans-serif; font-weight: 700;
    font-size: 66px; line-height: 0.98; color: var(--navy-deep);
  }
  .product-banner {
    position: absolute; left: 0; top: 404px; width: 372px; height: 78px;
    background: var(--red);
    clip-path: polygon(0 0, 92% 4%, 100% 12%, 90% 24%, 97% 40%, 88% 55%, 96% 72%, 86% 86%, 91% 100%, 0 100%);
    padding: 12px 0 0 30px;
    font-family: "Zilla Slab", serif; font-weight: 500; font-size: 23px;
    line-height: 1.08; letter-spacing: 1px; color: var(--white);
  }
  .features {
    position: absolute; left: 30px; top: 502px; list-style: none;
    font-family: "Nunito", sans-serif; font-style: italic; font-weight: 900;
    font-size: 16.5px; line-height: 20.6px; color: var(--navy-deep);
  }
  .features li::before { content: "★"; color: var(--red); font-style: normal; margin-right: 13px; font-size: 14px; }
  .product-window { position: absolute; left: 318px; top: 70px; width: 446px; height: 470px; }
  .pack-badge {
    position: absolute; left: 468px; top: 598px; width: 62px; height: 62px; border-radius: 50%;
    background: var(--apple); color: var(--white); text-align: center;
    font-family: "Fredoka", sans-serif; font-weight: 700; font-size: 20px; line-height: 0.9; padding-top: 13px;
  }
  .pack-badge small { font-size: 13px; display: block; }
  .cert { position: absolute; top: 596px; text-align: center; color: var(--white);
    font-family: "Nunito", sans-serif; font-style: normal; font-weight: 800; font-size: 7px; letter-spacing: .4px; }
  .cert .mark { width: 58px; height: 58px; margin: 0 auto 5px; border: 3px solid var(--white); }
  .cert-organic { left: 558px; width: 64px; }
  .cert-organic .mark { border-radius: 50%; }
  .cert-eco { left: 648px; width: 70px; }
  .cert-eco .mark { border-radius: 8px; background: var(--white); width: 50px; height: 50px; margin-bottom: 10px; }
</style>
</head>
<body>
<div class="canvas">
  <section class="box-front">
    <svg class="panel-shapes" width="770" height="680" viewBox="0 0 770 680" aria-hidden="true">
      <path d="M0 178 C120 120 260 60 420 42 C520 30 580 14 630 0 L770 0 L770 530 C600 570 450 640 300 662 C180 676 80 680 0 680 Z" fill="var(--kraft)"/>
      <path d="M0 178 C120 120 260 60 420 42 C520 30 580 14 630 0" fill="none" stroke="var(--red)" stroke-width="6"/>
      <rect x="80" y="0" width="34" height="58" fill="#3b45a8"/>
      <polygon points="80,150 114,150 114,205 97,190 80,205" fill="var(--navy)"/>
    </svg>

    <div class="seal">Nuvola<br>Serena</div>
    <div class="baby-tag">BABY</div>
    <h1 class="brand-name">Nuvola<br>Serena</h1>

    <div class="product-banner">MUSLIN SWADDLE<br>BLANKETS</div>

    <ul class="features">
      <li>100% certified organic cotton burp cloth</li>
      <li>Ultra-Soft, breathable, Hypoallergenic</li>
      <li>5 burp cloth per pack</li>
      <li>Suitable for baby delicate sensitive skin</li>
      <li>Super absorbent</li>
      <li>Made with love for little ones</li>
    </ul>

    <svg class="product-window" viewBox="0 0 446 470" role="img" aria-label="Die-cut window showing folded mint, pink and printed muslin cloths with a sleeping-baby and crescent moon illustration">
      <defs>
        <linearGradient id="clothTones" x1="0" y1="0" x2="1" y2="0">
          <stop offset="0" stop-color="var(--mint)"/>
          <stop offset=".35" stop-color="var(--blush)"/>
          <stop offset=".7" stop-color="#f6ece8"/>
          <stop offset="1" stop-color="var(--mint)"/>
        </linearGradient>
      </defs>
      <path d="M40 120 C30 60 90 20 170 30 C260 10 340 0 420 60 C440 140 440 260 420 340 C380 430 280 470 180 450 C90 430 40 360 30 270 C20 210 50 170 40 120 Z" fill="url(#clothTones)"/>
    </svg>

    <div class="pack-badge">2<small>pack</small></div>
    <div class="cert cert-organic"><div class="mark"></div>CERTIFIED ORGANIC</div>
    <div class="cert cert-eco"><div class="mark"></div>ECO-FRIENDLY</div>
  </section>
</div>
</body>
</html>
```